"Your Golden Years Start Tomorrow!" book cover for 80 page or so book.

Need a book cover that stands out on Bookvale, so highly engaging colors, need to reflect optimism, hope and determination. Go to Bookvale, type my name in and see the covers for the three other books I had written.

There's a lot of negativity and fear for Americans looking at retirement. Yet, they don't need that fear, my book tells them why they can be confident in their ability to retire.

There will be NO spine writing for the book, too small.

Target Market(s)

stressed out people in their 50s and 60s. This book appeals to working people, not high end, wealthy types.

Industry/Entity Type

Financial Planning

Colors

Designer to choose colors to be used in the design.

Requirements
Must have
• Needs to reflect simplicity in action.
• Please spell out my full name, MARK DELVORTH, at the bottom of the cover.
Nice to have
• if there is anyway to put a picture of an RV (Recreational Vehicle) that would be great.
Should not have
• Do NOT want to be the stodgy, typical financial planning literature out there. No guy in a suit and tie. No one sitting on a beach.
• Do not want my face on the cover either. (On the back yes.)

```html
<!DOCTYPE html>
<html lang="en">
<head>
<meta charset="utf-8">
<title>Your Golden Years Start Tomorrow! — Mark Delvorth</title>
<link rel="stylesheet" href="https://fonts.googleapis.com/css2?family=Crimson+Text:wght@400;600&display=swap">
<style>
  :root {
    --page: #ffffff;
    --cover-bg: #ffffff;
    --cover-edge: #8a877e;
    --ink-grey: #6e695c;
    --ink-gold: #c79d3c;
    --photo-top: #7fb069;
    --photo-mid: #e8e6df;
    --photo-low: #b9ab90;
  }
  html, body {
    margin: 0;
    padding: 0;
    width: 1200px;
    height: 1200px;
    overflow: hidden;
    background: var(--page);
  }
  .book-cover {
    position: absolute;
    left: 405px;
    top: 294px;
    width: 370px;
    height: 556px;
    box-sizing: border-box;
    background: var(--cover-bg);
    border: 1px solid var(--cover-edge);
    font-family: "Crimson Text", Georgia, serif;
    color: var(--ink-grey);
  }
  .book-title {
    margin: 0;
    font-weight: 400;
    font-size: inherit;
  }
  .title-line {
    position: absolute;
    left: 0;
    right: 0;
    text-align: center;
    line-height: 1;
    font-weight: 400;
    white-space: nowrap;
  }
  .title-line--grey { color: var(--ink-grey); }
  .title-line--gold { color: var(--ink-gold); }
  .title-line--first  { top: 38px;  font-size: 70px; }
  .title-line--second { top: 108px; font-size: 70px; }
  .title-line--last   { top: 346px; font-size: 72px; }

  .title-row {
    position: absolute;
    left: 0;
    right: 0;
    top: 234px;
    height: 50px;
    font-size: 46px;
    line-height: 1;
    font-weight: 400;
    color: var(--ink-grey);
    white-space: nowrap;
  }
  .title-row__left  { position: absolute; left: 12px; top: 0; }
  .title-row__right { position: absolute; left: 246px; top: 0; }

  .hero-photo {
    position: absolute;
    left: 116px;
    top: 176px;
    width: 124px;
    height: 153px;
    border-radius: 4px;
    background: linear-gradient(180deg, var(--photo-top) 0%, var(--photo-mid) 40%, var(--photo-low) 100%);
  }

  .author-name {
    position: absolute;
    left: 0;
    right: 0;
    top: 494px;
    margin: 0;
    text-align: center;
    font-size: 30px;
    line-height: 1;
    letter-spacing: 0.5px;
    font-weight: 400;
    color: var(--ink-grey);
  }
</style>
</head>
<body>
  <main class="book-cover">
    <h1 class="book-title">
      <span class="title-line title-line--grey title-line--first">Your</span>
      <span class="title-line title-line--gold title-line--second">Golden</span>
      <span class="title-row">
        <span class="title-row__left">Years</span>
        <span class="title-row__right">Start</span>
      </span>
      <span class="title-line title-line--gold title-line--last">Tomorrow!</span>
    </h1>
    <div class="hero-photo" role="img" aria-label="Smiling retired couple standing in front of a white RV with palm trees behind"></div>
    <p class="author-name">MARK DELVORTH</p>
  </main>
</body>
</html>
```